Winter Soccer Training

Youth Soccer Academy, I want to advertise Winter Training $195.00(Includes training for one month, Uniform) after first Month $145 per month.

Target Market(s)

kids from 5 years to 18

Industry/Entity Type

Training

Colors
3176b5

Requirements
Must have
• Winter Training
• Location: Maple Fieldhouse
• 48237 Brindle Oak rd Glendale MD 20769
• Phone:(555)874-9062
• Training Schedule
• Tuesday and Thursday
• 5:30pm to 6:30pm 5 to 10 years old
• 6:30pm to 7:30pm 11 to 15 years old
• 7:30pm to 8:30pm 16 to 19 years old
• www.quennitaacademy.com
Nice to have
• Soccer Field
Should not have
• Soccer Balls

```html
<!DOCTYPE html>
<html lang="en">
<head>
<meta charset="utf-8">
<title>Youth Soccer Winter Training – Postcard</title>
<link href="https://fonts.googleapis.com/css2?family=Russo+One&family=Signika:wght@400;600;700&display=swap" rel="stylesheet">
<style>
  :root {
    --brand-blue: #3176b5;
    --deep-blue: #0a4f8f;
    --title-blue: #1f63b8;
    --ink: #1e2a3a;
    --cream: #fff5d6;
    --paper: #ffffff;
    --backdrop: #ffffff;
    --pale-sky: #e6f1fb;
    --pale-grass: #dfeccd;
  }
  * { box-sizing: border-box; margin: 0; padding: 0; }
  html, body { width: 892px; height: 1200px; overflow: hidden; background: var(--backdrop); }
  body { position: relative; font-family: "Signika", sans-serif; color: var(--ink); }

  .card { position: absolute; left: 30px; width: 804px; height: 544px; overflow: hidden; background: var(--paper); }
  .card--front { top: 32px; }
  .card--back { top: 597px; }

  .front-art { position: absolute; inset: 0; }
  .panel { position: absolute; left: 545px; top: 0; width: 259px; height: 544px; color: #fff; text-align: center; }
  .panel__kicker { position: absolute; top: 52px; width: 100%; font-size: 28px; letter-spacing: 0.5px; }
  .panel__title { position: absolute; top: 86px; left: 50px; font-family: "Russo One", sans-serif; font-size: 38px; line-height: 36px; text-align: left; }
  .panel__days { position: absolute; top: 188px; width: 100%; font-size: 20px; }
  .panel__venue { position: absolute; top: 214px; width: 100%; font-size: 22px; }
  .panel__venue small { font-size: 16px; }
  .panel__ages { position: absolute; top: 244px; width: 100%; font-size: 21px; }
  .panel__name { position: absolute; top: 330px; left: 0; width: 100%; font-weight: 700; font-size: 26px; line-height: 30px; letter-spacing: 1px; color: #fff; }
  .panel__phone { position: absolute; top: 456px; left: 0; width: 100%; font-size: 26px; font-weight: 700; display: flex; justify-content: center; align-items: center; gap: 6px; }
  .panel__web { position: absolute; top: 494px; left: -10px; width: 279px; font-size: 17px; display: flex; justify-content: center; align-items: center; gap: 5px; }

  .back-art { position: absolute; inset: 0; background: linear-gradient(180deg, var(--pale-sky) 0%, #f4f9fe 55%, var(--pale-grass) 100%); }
  .back-figure { position: absolute; left: 560px; top: 60px; width: 200px; height: 420px; border-radius: 90px 90px 20px 20px; background: linear-gradient(180deg, #d5def0, #c9d3e6); opacity: 0.7; }
  .kid-figure { position: absolute; left: 26px; top: 296px; width: 111px; height: 208px; border-radius: 50px 50px 14px 14px; background: linear-gradient(180deg, #e0e4ea 0%, #d8453f 25%, #c8343a 48%, #2d4fae 60%, #e9ecf2 100%); }

  .name-mark { position: absolute; left: 30px; top: 50px; width: 110px; text-align: center; color: var(--title-blue); font-weight: 700; font-size: 18px; line-height: 22px; letter-spacing: 0.5px; }
  .heading { font-family: "Russo One", sans-serif; color: var(--title-blue); position: absolute; }
  .offer__title { left: 161px; top: 46px; font-size: 21px; }
  .offer__line { position: absolute; left: 161px; font-size: 17px; font-weight: 700; }
  .offer__line em { font-size: 13px; font-weight: 400; }
  .stamp { position: absolute; left: 650px; top: 48px; width: 107px; height: 105px; border: 1.5px dashed var(--title-blue); }
  .addr-line { position: absolute; left: 435px; width: 322px; border-top: 1.5px dashed var(--title-blue); }

  .section-title { font-size: 18px; }
  .list { position: absolute; font-size: 18px; line-height: 23.5px; }
  .contact { position: absolute; left: 155px; display: flex; align-items: center; gap: 6px; color: var(--title-blue); }
  .contact--phone { top: 450px; font-size: 24px; }
  .contact--web { top: 484px; font-size: 15px; }
</style>
</head>
<body>

<section class="card card--front">
  <svg class="front-art" width="804" height="544" viewBox="0 0 804 544">
    <defs>
      <linearGradient id="field" x1="0" y1="0" x2="0" y2="1">
        <stop offset="0" stop-color="#c9dcef"/>
        <stop offset="0.45" stop-color="#5d78b8"/>
        <stop offset="0.6" stop-color="#7ea347"/>
        <stop offset="1" stop-color="#4f7a2a"/>
      </linearGradient>
      <linearGradient id="panelGrad" x1="0" y1="0" x2="0" y2="1">
        <stop offset="0" stop-color="#1573bd"/>
        <stop offset="1" stop-color="#07508f"/>
      </linearGradient>
    </defs>
    <rect width="804" height="544" fill="url(#field)" role="img" aria-label="Photo of young players in blue kits running on a grass field"/>
    <path d="M525,0 C575,150 545,400 440,544 L804,544 L804,0 Z" fill="var(--cream)"/>
    <path d="M540,0 C590,150 560,400 455,544 L804,544 L804,0 Z" fill="url(#panelGrad)"/>
  </svg>

  <div class="panel">
    <div class="panel__kicker">YOUTH SOCCER</div>
    <div class="panel__title">WINTER<br>TRAINING</div>
    <div class="panel__days">TUESDAYS &amp; THURSDAYS</div>
    <div class="panel__venue"><small>at the</small> Maple Fieldhouse</div>
    <div class="panel__ages">AGES 5-18</div>
    <div class="panel__name">QUENNITA<br>ACADEMY</div>
    <div class="panel__phone">
      <svg width="22" height="22" viewBox="0 0 24 24" fill="none" stroke="#fff" stroke-width="2"><path d="M5 3h4l2 5-2.5 1.5a11 11 0 0 0 6 6L16 13l5 2v4a2 2 0 0 1-2 2A17 17 0 0 1 3 5a2 2 0 0 1 2-2z"/></svg>
      (555) 874-9062
    </div>
    <div class="panel__web">
      <svg width="17" height="17" viewBox="0 0 24 24" fill="none" stroke="#fff" stroke-width="2"><circle cx="12" cy="12" r="10"/><path d="M2 12h20M12 2c3 3 3 17 0 20M12 2c-3 3-3 17 0 20"/></svg>
      WWW.QUENNITAACADEMY.COM
    </div>
  </div>
</section>

<section class="card card--back">
  <div class="back-art" role="img" aria-label="Faded photo of a girl dribbling on a grass field"></div>
  <div class="back-figure"></div>
  <div class="kid-figure" role="img" aria-label="Cut-out photo of a young boy in a red shirt with his foot on a ball"></div>

  <div class="name-mark">QUENNITA<br>ACADEMY</div>
  <div class="heading offer__title">YOUTH SOCCER WINTER TRAINING</div>
  <div class="offer__line" style="top:80px">First Month $195 <em>(Includes Training &amp; Uniform)</em></div>
  <div class="offer__line" style="top:103px">Thereafter $145/month</div>
  <div class="stamp"></div>

  <div class="heading section-title" style="left:46px;top:155px">TRAINING SCHEDULE:</div>
  <div class="list" style="left:46px;top:183px">
    TUESDAY &amp; THURSDAY<br>
    5:30pm - 6:30pm Ages 5-10<br>
    6:30pm - 7:30pm Ages 11-15<br>
    7:30pm - 8:30pm Ages 16-19
  </div>

  <div class="addr-line" style="top:290px"></div>
  <div class="addr-line" style="top:348px"></div>
  <div class="addr-line" style="top:405px"></div>

  <div class="heading section-title" style="left:155px;top:300px">LOCATION:</div>
  <div class="list" style="left:155px;top:327px">
    Maple Fieldhouse<br>
    48237 Brindle Oak Rd<br>
    Glendale, MD 20769
  </div>

  <div class="heading section-title" style="left:155px;top:416px">DETAILS &amp; REGISTRATION:</div>
  <div class="contact contact--phone">
    <svg width="20" height="20" viewBox="0 0 24 24" fill="none" stroke="currentColor" stroke-width="2"><path d="M5 3h4l2 5-2.5 1.5a11 11 0 0 0 6 6L16 13l5 2v4a2 2 0 0 1-2 2A17 17 0 0 1 3 5a2 2 0 0 1 2-2z"/></svg>
    <span style="color:var(--ink)">(555) 874-9062</span>
  </div>
  <div class="contact contact--web">
    <svg width="15" height="15" viewBox="0 0 24 24" fill="none" stroke="currentColor" stroke-width="2"><circle cx="12" cy="12" r="10"/><path d="M2 12h20M12 2c3 3 3 17 0 20M12 2c-3 3-3 17 0 20"/></svg>
    <span style="color:var(--ink)">WWW.QUENNITAACADEMY.COM</span>
  </div>
</section>

</body>
</html>
```